ATTORNEY FULL PAGE AD

We need a full page flyer for our law firm. We are sending it to people who were in an auto accident and injured. I want to let people know that by hiring an attorney that does not mean that they are suing someone. We will just help them in filing a claim and to get them compensated for: medical bills, lost wages, car repairs, future medical treatment or surgery, and pain/suffering. They will NOT have to pay us any money unless we get them paid. I want to show that we are compassionate to the fact that they went through this tramatic event that will effect their lives for ever. They do not have to worry about anything once they hire us. Our website is: www.brightwelllawfirm.com Our colors are black and gold. NO GAMBLING REFERENCES!!!!
Updates

Don't worry so much about content and wording. Once we get a design and images that look great we will message you the exact words we would like put into the paragraphs. The overall "look" and images are the most important. If anyone has a great change-up logo we are open to it as well. Thanks for everyone's hard work!

We like the dark colors. Some of the images are a little cheesy. We are a family business and treat are clients as family. I like the pictures o the car crashes an the hands. No blood. We want to come off as respectful and trustworthy. It's more about how we will care for them as family than getting them lots of money. 

Target Market(s)

People who were in major accidents and have serious injuries

Industry/Entity Type

Attorney

Requirements
Must have
• Must have our phone number: 1-855-MBRIGHT
Website: www.brightwelllawfirm.com
Company name: Brightwell Law Group
Attorney name: Morgan Ellis Brightwell
High gloss with card stock paper.
Classy - NOT cheesy
Should not have
• No cartoons. Very masculine and professional. There may have been death involved in the accident so we want the ad to be very compassionate and moving.

```html
<!DOCTYPE html>
<html lang="en">
<head>
<meta charset="utf-8">
<title>Brightwell Law Group – Personal Injury Flyer</title>
<link href="https://fonts.googleapis.com/css2?family=Cinzel:wght@400;700&family=Roboto+Condensed:wght@400;700&family=Open+Sans:wght@400;600&family=Oswald:wght@400;500&family=Crimson+Text:ital,wght@1,600&display=swap" rel="stylesheet">
<style>
  :root {
    --ink: #0b0b0b;
    --gold: #f2a91e;
    --gold-text: #e9b640;
    --gold-pale: #f6c24d;
    --white: #ffffff;
    --grey-text: #d9d9d9;
    --rule: #5a4a22;
  }
  * { box-sizing: border-box; margin: 0; padding: 0; }
  html, body { width: 949px; height: 1200px; overflow: hidden; background: var(--ink); }
  .flyer {
    position: relative; width: 949px; height: 1200px; overflow: hidden;
    background: radial-gradient(ellipse at 40% 30%, #1c1c1c 0%, var(--ink) 70%);
    font-family: "Open Sans", sans-serif; color: var(--white);
  }
  .abs { position: absolute; }

  /* Brand name */
  .brand { left: 37px; top: 78px; display: flex; align-items: center; gap: 16px; }
  .brand-mark { width: 22px; height: 22px; background: var(--gold-text); }
  .brand-name {
    font-family: "Cinzel", serif; font-weight: 700; font-size: 36px;
    line-height: 42px; color: var(--gold-text); letter-spacing: 1px;
  }

  /* Headline */
  .headline {
    left: 35px; top: 206px;
    font-family: "Roboto Condensed", sans-serif; font-weight: 700;
    font-size: 64px; line-height: 62px; color: var(--white);
  }
  .tagline {
    left: 37px; top: 334px; width: 360px;
    font-family: "Cinzel", serif; font-size: 16px; line-height: 20px;
    color: var(--gold-text);
  }

  /* Photo placeholders */
  .photo { border-radius: 16px; }
  .photo-hero {
    left: 660px; top: 20px; width: 289px; height: 450px; border-radius: 0;
    background: linear-gradient(180deg, #111 0%, #3c4250 45%, #1a1c22 100%);
  }
  .photo-meeting {
    left: 37px; top: 423px; width: 396px; height: 211px;
    background: linear-gradient(135deg, #6e5a4e, #b79b8a 45%, #5e6b7a);
  }
  .photo-office {
    left: 37px; top: 797px; width: 396px; height: 213px;
    background: linear-gradient(135deg, #c9ccd1, #8a8f99 50%, #3e4350);
  }

  /* Practice list */
  .practice { left: 484px; top: 218px; width: 300px; }
  .practice h2 {
    font-family: "Cinzel", serif; font-weight: 400; font-size: 19px;
    color: var(--gold-text); letter-spacing: 1px;
    border-bottom: 1px solid var(--rule); padding-bottom: 6px; margin-bottom: 4px;
  }
  .practice li {
    list-style: none; font-family: "Roboto Condensed", sans-serif;
    font-size: 15px; color: var(--gold-text); line-height: 25px;
    border-bottom: 1px solid var(--rule); width: 190px;
  }

  /* Gold banners */
  .banner {
    background: var(--gold); color: var(--ink);
    font-family: "Cinzel", serif; font-weight: 700;
    display: flex; align-items: center;
  }
  .banner-about {
    left: 480px; top: 469px; width: 469px; height: 35px;
    border-radius: 18px 0 0 18px; padding-left: 34px; font-size: 19px;
  }
  .banner-team {
    left: 480px; top: 764px; width: 469px; height: 35px;
    border-radius: 18px 0 0 18px; padding-left: 28px; font-size: 19px;
  }
  .banner-call {
    left: 0; top: 1024px; width: 445px; height: 36px;
    border-radius: 0 18px 18px 0; padding-left: 37px;
    font-family: "Crimson Text", serif; font-style: italic; font-weight: 600; font-size: 20px;
  }

  /* Copy */
  .copy p { font-size: 12px; line-height: 16px; color: var(--grey-text); margin-bottom: 10px; }
  .copy-about { left: 484px; top: 516px; width: 442px; text-align: justify; }
  .copy-care { left: 37px; top: 648px; width: 400px; }

  /* Team */
  .team { left: 482px; top: 807px; width: 420px; display: grid;
    grid-template-columns: repeat(3, 120px); column-gap: 30px; }
  .member { text-align: center; height: 177px; }
  .member .portrait {
    width: 120px; height: 126px; border-radius: 12px;
    border: 2px solid #9a9a9a;
    background: linear-gradient(180deg, #8c8c8c, #3a3a3a);
  }
  .member .name { font-family: "Roboto Condensed", sans-serif; font-size: 12px; margin-top: 6px; color: var(--white); white-space: nowrap; }
  .member .role { font-size: 9px; line-height: 11px; color: var(--gold-text); }

  /* Phones */
  .phone { left: 37px; font-family: "Oswald", sans-serif; color: var(--gold-pale); line-height: 1; }
  .phone .label { font-weight: 400; font-size: 30px; }
  .phone .number { font-weight: 500; font-size: 40px; color: var(--white); }
  .phone-local { top: 1070px; }
  .phone-toll { top: 1116px; }

  /* Footer strip */
  .footer {
    left: 0; top: 1163px; width: 949px; height: 37px; background: var(--gold);
    color: var(--ink); display: flex; align-items: center;
    font-family: "Roboto Condensed", sans-serif;
  }
  .footer .web { margin-left: 37px; font-size: 15px; letter-spacing: 3px; width: 410px; }
  .footer .addr { font-size: 15px; }
  .footer .addr strong { font-size: 19px; font-weight: 700; }
</style>
</head>
<body>
<main class="flyer">
  <div class="abs photo photo-hero" role="img" aria-label="Smiling attorney in a suit reaching out for a handshake"></div>

  <div class="abs brand">
    <span class="brand-mark"></span>
    <span class="brand-name">BRIGHTWELL<br>LAW GROUP</span>
  </div>

  <h1 class="abs headline">INJURED?<br>We can HELP</h1>
  <p class="abs tagline">They do not have to worry about anything once they hire us</p>

  <section class="abs practice">
    <h2>PERSONAL INJURY</h2>
    <ul>
      <li>AUTO ACCIDENT</li>
      <li>DUI ACCIDENT</li>
      <li>MEDICAL MALPRACTICE</li>
      <li>PHARMACEUTICAL INJURY</li>
      <li>DOG BITE</li>
      <li>WORKER'S COMPENSATION</li>
      <li>PREMISE INJURY</li>
    </ul>
  </section>

  <div class="abs photo photo-meeting" role="img" aria-label="Attorney consulting with two clients at a table"></div>

  <div class="abs banner banner-about">WHAT IS BRIGHTWELL LAW GROUP?</div>
  <div class="abs copy copy-about">
    <p>The Brightwell Law Group is a personal injury law firm based in Savannah, Georgia. Our dedicated team of attorneys and staff is here to assist you with the following personal injury claims.</p>
    <p>Car accidents, big truck accidents, DUI injury accidents, motorcycle accident, pedestrian accident injury, passenger accident injury, worker's compensation, medical malpractice, nursing home abuse, dog bite injury, hospital injury, dental injury, pharmaceutical injury and premise injury, as well as several other injury claims.</p>
    <p>If you decide on Brightwell Law Group to handle your personal injury claim, you pay no money out of your pocket unless we win your case. Call the Brightwell Law Group now for a free, informational consultation to discuss your personal injury claim.</p>
  </div>

  <div class="abs copy copy-care">
    <p>At Brightwell Law Group, we sincerely care about our clients. When you step into our office, you become family, and we fight hard to win our family the recovery it deserves.</p>
    <p>We are sending it to people who were in an auto accident and injured. We will just help them in filing a claim and to get them compensated for: medical bills, lost wages, car repairs, future medical treatment or surgery, and pain/suffering.</p>
  </div>

  <div class="abs photo photo-office" role="img" aria-label="Professional woman in front of colleagues in a meeting room"></div>

  <div class="abs banner banner-team">BRIGHTWELL LAW GROUP TEAM</div>
  <section class="abs team">
    <div class="member"><div class="portrait" role="img" aria-label="Portrait of Morgan Brightwell"></div><div class="name">MORGAN BRIGHTWELL</div><div class="role">(CEO and Lead Attorney)</div></div>
    <div class="member"><div class="portrait" role="img" aria-label="Portrait of Daniel Reyes"></div><div class="name">DANIEL REYES</div><div class="role">(Attorney)</div></div>
    <div class="member"><div class="portrait" role="img" aria-label="Portrait of Marcus Hale"></div><div class="name">MARCUS HALE</div><div class="role">(Personal Injury Department Manager/Office Manager)</div></div>
    <div class="member"><div class="portrait" role="img" aria-label="Portrait of Nora Whitfield"></div><div class="name">NORA WHITFIELD</div><div class="role">(Criminal Department Manager)</div></div>
    <div class="member"><div class="portrait" role="img" aria-label="Portrait of Alison Kerr"></div><div class="name">ALISON KERR</div><div class="role">(Personal Injury Case Manager)</div></div>
    <div class="member"><div class="portrait" role="img" aria-label="Portrait of Jake Porter"></div><div class="name">JAKE PORTER</div><div class="role">(Creative Director of Advertising)</div></div>
  </section>

  <div class="abs banner banner-call">Call us today to schedule a free consultation</div>
  <div class="abs phone phone-local"><span class="label">Local: </span><span class="number">912-555-0147</span></div>
  <div class="abs phone phone-toll"><span class="label">Toll free: </span><span class="number">855-MBRIGHT</span></div>

  <footer class="abs footer">
    <span class="web">www.BRIGHTWELLLAWFIRM.com</span>
    <span class="addr">418 Harbor Street, Savannah, GA 31401. &nbsp;T: <strong>(855) 555-0192</strong></span>
  </footer>
</main>
</body>
</html>
```